App-Design für Vergleichsportal für Reparaturen
Zielgruppe
Flickwerkstolz ist das Vergleichsportal für Reparaturen in deiner Nähe. Egal ob du eine Werkstatt für dein Smartphone, Tablet, Laptop, Computer, Smartwatch oder Spielkonsole suchst. Mit uns findest du deine passende Reparaturwerkstat in deiner Nähe mit dem besten Preis für dich. Du kannst dich direkt über unser Portal deinen Reparaturauftrag erhalten und wirst durch unser Lumen Kaufhut Käuferschutz und unser VORIBA Treuhandschutz abgesichert.
Aufgabenstellung
Unter Flickwerkstolz.de kann das aktuelle Design angeschaut werden. Die Farbe sollten übernommen werden.
Über die Startseite kann der Kunde sein Gerät, Service sowie seine Adresse eingeben. Auf der Vergleichsseite bekommt der Kunde die Übersicht welche Reparaturwerkstätten es gibt, zu welche Preisen die ausgewählte Dienstleistung angeboten wird. Wenn der Kunde auf den Button 'Jetzt Online Bestpreis buchen' drückt, dann kommt der Kunde in den Warenkorb. Im Warenkorb können noch weitere Dienstleistungen und Produkte dazugebucht werden. Und anschließend kommt der Kunde in die Kasse und kann der Bestellvorgang beenden. Die Benutzerführung sollte einfach sein. Im Fokus steht die Vergleichsseite. Dort sollte der Kunde ca. 4 Werkstätten auf einen Blick sehen können. Könnte ausschauen wie bei Preisluke7 in der Kategorie Mobilfunk.
Die Vergleichseite sollte auf jeden Fall folgende Elemente enthalten:
- Entfernung zur Werkstatt in Meter bzw. Kilometer
- Logo der Werkstatt
- Name der Werkstatt
- Bewertungssterne der Werkstatt
- Reparaturzeit und Ersatzeilverfügbarkeit
- Reparaturpreis (Platz sollte auch bei Auswahl von 2 Dienstleistungen vorhanden sein)
- Rabattanzeige
- Qualitätssiegel (noch nicht vorhanden)
- Anzeige von Verknappung (z. B. noch 3 Termin frei)
- Qualitätsmerkmale (z. B. 12 Monate Garantie)
Die Merkmale Öffnungszeiten, Adresse, Kostenpflichtige Zusatzleistungen können aus Platzgründen in den Warenkorbseite wandern außer es gibt eine schöne und einfache Lösung.
In der Warenkorbseite kann dazu auch die Preisluke7 Seite dienen.
Bei allen sollte auf die Benutzerfreundlichkeit geachtet werden.
Bei offenen Frage stehe ich zur Verfügung und freue mich auf viele Designs.
Vielen DANK im Voraus!

```html
<!DOCTYPE html>
<html lang="de">
<head>
<meta charset="utf-8">
<title>Flickwerkstolz – Vergleichsseite</title>
<link href="https://fonts.googleapis.com/css2?family=Nunito+Sans:wght@400;600;700&display=swap" rel="stylesheet">
<style>
:root{
  --bg:#232323;
  --white:#ffffff;
  --body:#e8ebee;
  --navy:#2b4a5b;
  --cookie:#3b4045;
  --green:#8cc63f;
  --red:#e2231a;
  --star:#f5c400;
  --star-empty:#d5d5d5;
  --text:#2c2f33;
  --muted:#555a60;
}
*{box-sizing:border-box;margin:0;padding:0}
html,body{width:1200px;height:728px;overflow:hidden;background:var(--bg)}
body{font-family:"Nunito Sans",Arial,sans-serif;color:var(--text)}
.frame{position:absolute;left:432px;top:0;width:336px;height:728px;overflow:hidden}
.screen{position:absolute;left:0;top:0;width:402px;height:870px;background:var(--body);transform:scale(.8368);transform-origin:0 0;overflow:hidden}
.status{height:30px;background:var(--white);display:flex;justify-content:space-between;align-items:center;padding:6px 16px 0 18px;font-size:15px;font-weight:600}
.status svg{display:block}
.topbar{height:57px;background:var(--white);display:flex;justify-content:space-between;align-items:center;padding:0 14px 8px 16px}
.brand{display:flex;align-items:center;gap:7px;font-size:17px;color:var(--navy);font-weight:400}
.brand i{width:12px;height:12px;border-radius:50%;background:var(--green);display:block}
.menu{width:24px;height:16px;display:flex;flex-direction:column;justify-content:space-between}
.menu span{height:2px;background:var(--navy)}
.cookie{height:31px;background:var(--cookie);color:#e6e6e6;font-size:8px;display:flex;align-items:center;justify-content:space-between;padding:0 32px 0 31px}
.cookie em{font-style:normal;color:var(--green)}
.cookie .ok{background:var(--green);color:var(--white);font-size:7.5px;padding:5px 6px;border-radius:1px}
.steps{height:62px;background:var(--navy);position:relative;color:#e4e9ec;font-size:10.5px}
.steps .line{position:absolute;left:69px;right:66px;top:24px;height:1px;background:#e4e9ec}
.step{position:absolute;top:14px;text-align:center;width:110px;margin-left:-55px}
.step .dot{width:17px;height:17px;border-radius:50%;border:1px solid #e4e9ec;background:var(--navy);margin:1px auto 6px;font-size:10px;line-height:15px}
.step.active .dot{width:24px;height:24px;margin:-3px auto 3px;background:var(--green);border:3px solid #dfe6ea;line-height:18px;color:var(--white)}
.step.active{color:var(--green)}
.crumb{display:flex;justify-content:space-between;padding:12px 32px 0 31px;font-size:9.5px;height:39px}
.crumb a{color:var(--green);text-decoration:none}
.card{position:absolute;left:31px;width:339px;background:var(--white);border:1px solid #c9d0d5}
.card-head{height:27px;background:var(--navy);color:var(--white);font-size:12.5px;display:flex;align-items:center;justify-content:space-between;padding:0 12px 0 7px}
.card-body{padding:11px 11px 0 11px;position:relative}
.name{font-size:13.5px}
.logo{display:flex;align-items:center;gap:5px;margin-top:6px;height:22px;font-size:17px;color:var(--navy);font-weight:600}
.logo i{width:16px;height:16px;background:var(--navy);display:block}
.stars{display:flex;align-items:center;gap:3px;margin-top:4px;color:var(--star);font-size:13px}
.stars svg{width:17px;height:17px}
.price{position:absolute;right:11px;top:8px;text-align:right}
.old{font-size:18px;text-decoration:line-through;color:var(--text)}
.new{font-size:22px;color:var(--red);line-height:1.1}
.plain{font-size:22px;color:var(--text);margin-top:14px}
.deal{display:flex;align-items:center;gap:6px;justify-content:flex-end;margin-top:4px;font-size:8.5px;color:var(--green);line-height:1.05;text-align:center}
.info{display:flex;justify-content:space-between;margin-top:22px;font-size:10px}
.facts{display:grid;grid-template-columns:66px 1fr;row-gap:1px}
.facts dt{color:var(--muted);font-size:9px}
.perks li{list-style:none;display:flex;align-items:center;gap:5px;margin-bottom:6px}
.perks svg{width:14px;height:14px}
.scarce{text-align:center;color:var(--red);font-size:12px;margin-top:22px;display:flex;justify-content:center;align-items:center;gap:8px}
.book{margin:14px 0 0;height:35px;background:var(--green);color:var(--white);font-size:16px;display:flex;align-items:center;justify-content:center;gap:9px}
</style>
</head>
<body>
<div class="frame">
<div class="screen">
  <div class="status"><span>9:41</span>
    <svg width="62" height="12" viewBox="0 0 62 12"><rect x="0" y="8" width="3" height="4" fill="#333"/><rect x="4" y="6" width="3" height="6" fill="#333"/><rect x="8" y="3" width="3" height="9" fill="#333"/><rect x="12" y="0" width="3" height="12" fill="#333"/><path d="M22 4a10 10 0 0 1 14 0l-2 2a7 7 0 0 0-10 0zM25 7a5 5 0 0 1 8 0l-4 4z" fill="#333"/><rect x="40" y="1" width="20" height="10" rx="2" fill="none" stroke="#333"/><rect x="42" y="3" width="16" height="6" fill="#333"/></svg>
  </div>
  <header class="topbar">
    <div class="brand"><i></i>flickwerkstolz</div>
    <div class="menu"><span></span><span></span><span></span></div>
  </header>
  <div class="cookie"><span>Wir verwenden <em>Cookies</em> und erhalten <em>Abschlussprovisionen</em> von Anbietern.</span><span class="ok">Einverstanden</span></div>
  <nav class="steps">
    <div class="line"></div>
    <div class="step active" style="left:69px"><div class="dot">1</div>Werkstatt wählen</div>
    <div class="step" style="left:201px"><div class="dot">2</div>Zahlung durchführen</div>
    <div class="step" style="left:337px"><div class="dot">3</div>Gerät abgeben</div>
  </nav>
  <div class="crumb"><span>Lumo 6s / Akku / Lindenplatz 4, Ahornstadt</span><a href="#">✎ Adresse ändern</a></div>

  <svg width="0" height="0" style="position:absolute"><defs>
    <symbol id="star" viewBox="0 0 24 24"><path d="M12 2l3 6.5 7 .8-5.2 4.8 1.5 7L12 17.6 5.7 21.1l1.5-7L2 9.3l7-.8z"/></symbol>
    <symbol id="pin" viewBox="0 0 24 24"><path d="M12 2a6 6 0 0 0-6 6c0 5 6 13 6 13s6-8 6-13a6 6 0 0 0-6-6zm0 8.5a2.5 2.5 0 1 1 0-5 2.5 2.5 0 0 1 0 5z" fill="#fff"/></symbol>
    <symbol id="flag" viewBox="0 0 24 24"><path d="M5 4h14v8H9l-2 2v7H5z" fill="#fff"/></symbol>
    <symbol id="cart" viewBox="0 0 24 24"><path d="M2 4h3l2.5 11h11l2-8H7" fill="none" stroke="#fff" stroke-width="1.8"/><circle cx="9" cy="19" r="1.6" fill="#fff"/><circle cx="17" cy="19" r="1.6" fill="#fff"/></symbol>
    <symbol id="tool" viewBox="0 0 24 24"><path d="M3 12h8l3-3 3 3-3 3-3-3M15 6l3-3 3 3-3 3" fill="none" stroke="#444" stroke-width="1.5"/></symbol>
    <symbol id="shield" viewBox="0 0 24 24"><path d="M12 3l7 3v6c0 4-3 7-7 9-4-2-7-5-7-9V6z" fill="none" stroke="#444" stroke-width="1.5"/></symbol>
    <symbol id="seal" viewBox="0 0 24 24"><circle cx="12" cy="9" r="6" fill="none" stroke="#444" stroke-width="1.5"/><path d="M8 14l-2 7 6-3 6 3-2-7" fill="none" stroke="#444" stroke-width="1.5"/></symbol>
  </defs></svg>

  <article class="card" style="top:219px;height:286px">
    <div class="card-head"><svg width="14" height="14"><use href="#pin"/></svg>246 m von dir entfernt<svg width="12" height="12"><use href="#flag"/></svg></div>
    <div class="card-body">
      <div class="name">Kelvor Repair München</div>
      <div class="logo"><i></i>KELVOR</div>
      <div class="stars"><svg fill="var(--star)"><use href="#star"/></svg><svg fill="var(--star)"><use href="#star"/></svg><svg fill="var(--star)"><use href="#star"/></svg><svg fill="var(--star)"><use href="#star"/></svg><svg fill="var(--star)"><use href="#star"/></svg>(5/5)</div>
      <div class="price"><div class="old">87,00€</div><div class="new">79,00€</div>
        <div class="deal"><svg width="20" height="20" viewBox="0 0 20 20"><circle cx="10" cy="10" r="8.5" fill="none" stroke="var(--green)" stroke-width="1.5"/><path d="M7 13l6-6" stroke="var(--green)" stroke-width="1.3"/><circle cx="7.5" cy="7.5" r="1.2" fill="var(--green)"/><circle cx="12.5" cy="12.5" r="1.2" fill="var(--green)"/></svg><span>-8,00€ Rabatt<br>endet in 13h</span></div>
      </div>
      <div class="info">
        <dl class="facts"><dt>Adresse:</dt><dd>Almenweg 5<br>80111 Ahornstadt</dd><dt>Reparaturzeit:</dt><dd>2 Tage</dd><dt>Ersatzteil:</dt><dd>Verfügbar</dd></dl>
        <ul class="perks"><li><svg><use href="#tool"/></svg>kostenlos 30 min.</li><li><svg><use href="#shield"/></svg>12 Monate Garantie</li><li><svg><use href="#seal"/></svg>Muster Siegel</li></ul>
      </div>
      <div class="scarce"><svg width="20" height="18" viewBox="0 0 20 18"><path d="M10 1l9 16H1z" fill="none" stroke="var(--red)" stroke-width="1.5"/><path d="M10 6v6M10 13.5v1.5" stroke="var(--red)" stroke-width="1.5"/></svg>nur noch 3 Termine frei !</div>
      <div class="book"><svg width="20" height="20"><use href="#cart"/></svg>Jetzt Online Bestpreis buchen</div>
    </div>
  </article>

  <article class="card" style="top:516px;height:255px">
    <div class="card-head"><svg width="14" height="14"><use href="#pin"/></svg>762 m von dir entfernt<svg width="12" height="12"><use href="#flag"/></svg></div>
    <div class="card-body">
      <div class="name">Varnhof Handydienst Süd</div>
      <div class="logo"><i></i>VARNHOF</div>
      <div class="stars"><svg fill="var(--star)"><use href="#star"/></svg><svg fill="var(--star)"><use href="#star"/></svg><svg fill="var(--star)"><use href="#star"/></svg><svg fill="var(--star)"><use href="#star"/></svg><svg fill="var(--star-empty)"><use href="#star"/></svg>(3,7/5)</div>
      <div class="price"><div class="plain">82,00€</div></div>
      <div class="info" style="margin-top:20px">
        <dl class="facts"><dt>Adresse:</dt><dd>Almenweg 5<br>80111 Ahornstadt</dd><dt>Reparaturzeit:</dt><dd>2 Tage</dd><dt>Ersatzteil:</dt><dd>Verfügbar</dd></dl>
        <ul class="perks"><li><svg><use href="#tool"/></svg>kostenlos 90 min.</li><li><svg><use href="#shield"/></svg>12 Monate Garantie</li><li><svg><use href="#seal"/></svg>Muster Siegel</li></ul>
      </div>
      <div class="book" style="margin-top:12px"><svg width="20" height="20"><use href="#cart"/></svg>Jetzt Online Bestpreis buchen</div>
    </div>
  </article>

  <article class="card" style="top:780px;height:100px">
    <div class="card-head"><svg width="14" height="14"><use href="#pin"/></svg>1,2 km von dir entfernt<svg width="12" height="12"><use href="#flag"/></svg></div>
    <div class="card-body">
      <div class="name">Morvo Shop am Anger</div>
      <div class="logo"><i></i>MORVO</div>
      <div class="price"><div class="old">100,00€</div><div class="new">89,00€</div></div>
    </div>
  </article>
</div>
</div>
</body>
</html>
```